Non-governmental organisation branding design

We are looking to get the branding for our new NGO:

Kestrel Harbour Centre

Our tag-line is: Peace through dialogue

We are a peace brokering organisation that conducts research and offers peace brokering services relating to conflicts around the world.

The branding needs to be simple, to the point and serious.

Other comparable organisations are:

https://www.vantrellhub.org/

http://tlx.fi/

https://www.oravelle.org/

Any questions, please get in touch.

Logo Text

Kestrel Harbour Centre

Number of Pages Required

1 page

```html
<!DOCTYPE html>
<html lang="en">
<head>
<meta charset="utf-8">
<title>Kestrel Harbour Centre</title>
<link href="https://fonts.googleapis.com/css2?family=Lato:wght@400;700;900&family=Roboto:wght@400;500;700&display=swap" rel="stylesheet">
<style>
:root{
  --blue:#2f6fe0;
  --blue-text:#2a64d6;
  --sky:#8cc6f2;
  --band-light:#80bdf6;
  --band:#3d7ff0;
  --ink:#2b2b2b;
  --dark:#1b1d1f;
  --white:#ffffff;
}
*{margin:0;padding:0;box-sizing:border-box}
html,body{width:1200px;height:1200px;overflow:hidden;background:var(--white)}
body{position:relative;font-family:'Lato',sans-serif;color:var(--ink)}
.abs{position:absolute}
.logo{left:252px;top:11px;font-family:'Roboto',sans-serif;font-weight:700;font-size:15px;line-height:15px;color:var(--blue)}
.logo .dot{display:inline-block;width:9px;height:9px;border-radius:50%;background:var(--blue);margin-right:4px;vertical-align:middle}
.nav{left:114px;top:54px;display:flex;gap:14px;font-size:7px;letter-spacing:.1px;color:var(--ink)}
.nav span{padding-bottom:5px}
.nav .active{border-bottom:2px solid var(--blue)}
.hero-panel{left:0;top:68px;width:186px;height:275px;background:var(--dark)}
.hero-photo{left:186px;top:68px;width:425px;height:275px;background:linear-gradient(160deg,#0b0f24 0%,#1e2350 35%,#7a5a2a 65%,#1b2030 100%)}
.hero-title{left:32px;top:128px;font-family:'Roboto',sans-serif;font-weight:400;font-size:20px;line-height:23px;color:var(--sky)}
.hero-body{left:32px;top:189px;width:142px;font-size:6.8px;line-height:10.7px;color:#e8e8e8}
.hero-more{left:32px;top:251px;font-size:6.8px;font-weight:900;color:var(--white)}
.sect-head{font-family:'Roboto',sans-serif;font-weight:700;font-size:13px;letter-spacing:6.5px;line-height:16px;color:var(--blue)}
.about-head{left:55px;top:372px}
.about-body{left:55px;top:423px;width:338px;font-size:7.1px;line-height:9.8px}
.link{font-size:6.8px;font-weight:900;color:var(--blue-text)}
.about-photo{left:418px;top:343px;width:143px;height:188px;background:linear-gradient(180deg,#0d1320 0%,#243248 45%,#b9a98c 70%,#1a2232 100%)}
.news-head{left:55px;top:594px}
.tri{width:118px;height:117px}
.tri-a{clip-path:polygon(0 0,0 100%,100% 100%)}
.tri-b{clip-path:polygon(0 0,100% 0,100% 100%)}
.num{font-family:'Roboto',sans-serif;font-weight:500;font-size:34px;line-height:34px;color:var(--blue)}
.card-title{font-size:7.5px;font-weight:700;color:var(--blue-text)}
.card-body{width:158px;font-size:7.1px;line-height:9.8px}
.touch-art{left:42px;top:1010px;width:190px;height:140px;border-radius:50%;background:radial-gradient(ellipse at center,#8ac2ad 0%,#cfe6dd 55%,#ffffff 75%)}
.touch-head{left:265px;top:1014px}
.touch-body{left:262px;top:1058px;width:268px;font-size:7.1px;line-height:9.8px}
.create-head{left:666px;top:41px}
.photo{top:99px;width:161px;height:182px}
.date{right:7px;bottom:9px;font-family:'Roboto',sans-serif;font-weight:700;font-size:9.5px;line-height:11px;text-align:right;color:var(--white)}
.post-title{top:294px;width:150px;font-family:'Roboto',sans-serif;font-weight:700;font-size:8px;line-height:11px;color:var(--blue-text)}
.post-body{top:326px;width:150px;font-size:6.8px;line-height:8.7px}
.post-more{top:383px}
.contact{left:611px;top:434px;width:193px;height:157px;background:var(--band-light)}
.map{left:804px;top:434px;width:396px;height:157px;background:linear-gradient(120deg,#bfe7f2 0%,#dfeccf 40%,#f3e9b8 60%,#bfe7f2 100%)}
.contact-head{left:666px;top:484px;font-family:'Roboto',sans-serif;font-weight:700;font-size:8.5px;letter-spacing:4px;line-height:11px;color:var(--white)}
.contact-info{left:666px;top:514px;font-size:6.8px;font-weight:700;line-height:11px;color:var(--white)}
.footer{left:611px;top:591px;width:589px;height:131px;background:var(--band)}
.foot-head{top:609px;font-family:'Roboto',sans-serif;font-weight:700;font-size:8.5px;letter-spacing:4px;line-height:10.5px;color:var(--white)}
.foot-col{top:609px;font-size:5px;line-height:6.4px;color:#e9f1ff}
.foot-col b{font-weight:900;color:var(--white)}
.social{top:696px;width:17px;height:17px;border-radius:50%;background:var(--white)}
.rights{right:28px;top:701px;font-size:6.8px;color:var(--white)}
</style>
</head>
<body>
<div class="abs logo"><span class="dot"></span>Kestrel Harbour<br>&nbsp;&nbsp;&nbsp;&nbsp;Centre</div>
<nav class="abs nav"><span class="active">WHO WE ARE</span><span>WHERE WE WORK</span><span>WHAT WE DO</span><span>GET INVOLVED</span><span>ANNOUNCEMENTS</span><span>CONTACT US</span></nav>

<section>
  <div class="abs hero-panel"></div>
  <div class="abs hero-photo" role="img" aria-label="Night photograph of a harbour city skyline with a fountain statue"></div>
  <h1 class="abs hero-title">Peace through<br>dialogue</h1>
  <p class="abs hero-body">Lorem ipsum dolor sit amet, consectetuer adipiscing elit. Aenean commodo ligula eget dolor. Aenean massa. Cum sociis natoque penatibus et magnis dis parturient montes,</p>
  <div class="abs hero-more">READ MORE</div>
</section>

<section>
  <h2 class="abs sect-head about-head">Kestrel<br>Harbour Centre</h2>
  <p class="abs about-body">Lorem ipsum dolor sit amet, consectetuer adipiscing elit. Aenean commodo ligula eget dolor. Aenean massa. Cum sociis natoque penatibus et magnis dis parturient montes, nascetur ridiculus mus. Donec quam felis, ultricies nec, pellentesque eu, pretium quis, sem. Nulla consequat massa quis enim. Donec pede justo, fringilla vel, aliquet nec, vulputate eget, arcu. In enim justo, rhoncus ut, imperdiet a, venenatis vitae, justo. Nullam dictum felis eu pede mollis pretium. Integer tincidunt. Cras dapibus. Vivamus elementum semper nisi. Aenean vulputate eleifend tellus. Aenean leo ligula, porttitor eu, consequat vitae, eleifend ac, enim. Aliquam lorem ante, dapibus in, viverra quis, feugiat a,</p>
  <div class="abs link" style="left:55px;top:516px">READ MORE</div>
  <div class="abs about-photo" role="img" aria-label="Night photograph of towers behind a fountain statue"></div>
</section>

<section>
  <h2 class="abs sect-head news-head">NEWS<br>UPDATES</h2>

  <div class="abs tri tri-a" style="left:50px;top:659px;background:linear-gradient(180deg,#1a1a2a,#8a2a1a 55%,#c46a2a)" role="img" aria-label="Photograph of a lit temple at night"></div>
  <div class="abs num" style="left:117px;top:664px">1</div>
  <div class="abs card-title" style="left:139px;top:673px">LOREM IPSUM</div>
  <p class="abs card-body" style="left:139px;top:689px">Lorem ipsum dolor sit amet, consectetuer adipiscing elit. Aenean commodo ligula eget dolor. Aenean massa. Cum sociis natoque penatibus et magnis dis parturient montes, nascetur ridiculus</p>

  <div class="abs tri tri-a" style="left:311px;top:659px;background:linear-gradient(180deg,#10141c,#3a2a5a 55%,#1c2a3a)" role="img" aria-label="Photograph of a waterfront building at night"></div>
  <div class="abs num" style="left:373px;top:664px">2</div>
  <div class="abs card-title" style="left:399px;top:673px">LOREM IPSUM</div>
  <p class="abs card-body" style="left:399px;top:689px">Lorem ipsum dolor sit amet, consectetuer adipiscing elit. Aenean commodo ligula eget dolor. Aenean massa. Cum sociis natoque penatibus et magnis dis parturient montes, nascetur ridiculus</p>

  <div class="abs tri tri-b" style="left:182px;top:790px;background:linear-gradient(200deg,#0c1030,#3a2a7a 50%,#10142a)" role="img" aria-label="Photograph of an observation wheel at night"></div>
  <div class="abs num" style="left:54px;top:835px">3</div>
  <div class="abs card-title" style="left:84px;top:845px">LOREM IPSUM</div>
  <p class="abs card-body" style="left:84px;top:861px">Lorem ipsum dolor sit amet, consectetuer adipiscing elit. Aenean commodo ligula eget dolor. Aenean massa. Cum sociis natoque penatibus et magnis dis parturient montes, nascetur ridiculus</p>

  <div class="abs tri tri-b" style="left:439px;top:790px;background:linear-gradient(200deg,#2a4a20,#5a7a3a 45%,#d8d8d8)" role="img" aria-label="Photograph of a bus on a tree-lined street"></div>
  <div class="abs num" style="left:316px;top:835px">4</div>
  <div class="abs card-title" style="left:340px;top:845px">LOREM IPSUM</div>
  <p class="abs card-body" style="left:340px;top:861px">Lorem ipsum dolor sit amet, consectetuer adipiscing elit. Aenean commodo ligula eget dolor. Aenean massa. Cum sociis natoque penatibus et magnis dis parturient montes, nascetur ridiculus</p>

  <div class="abs link" style="left:511px;top:942px">LEARN MORE</div>
</section>

<section>
  <div class="abs touch-art" role="img" aria-label="Illustration of a world map with a clipboard and communication icons"></div>
  <h2 class="abs sect-head touch-head">GET IN<br>TOUCH</h2>
  <p class="abs touch-body">Lorem ipsum dolor sit amet, consectetuer adipiscing elit. Aenean commodo ligula eget dolor. Aenean massa. Cum sociis natoque penatibus et magnis dis parturient montes, nascetur ridiculus mus. Donec quam felis, ultricies nec, pellentesque eu, pretium quis, sem. Nulla consequat massa quis enim. Donec pede justo, fringilla vel, aliquet nec, vulputate eget, arcu. In enim justo, rhoncus ut, imperdiet a, venenatis vitae, justo. Nullam dictum felis eu pede mollis pretium. Integer tincidunt. Cras dapibus. Vivamus elementum semper nisi. Aenean vulputate eleifend tellus. Aenean leo ligula, porttitor eu, consequat vitae, eleifend ac, enim. Aliquam lorem</p>
  <div class="abs link" style="left:262px;top:1157px">VIEW PROCESS</div>
</section>

<section>
  <h2 class="abs sect-head create-head">WHAT WE<br>CREATE</h2>

  <div class="abs photo" style="left:662px;background:linear-gradient(150deg,#2a2d33 0%,#e8ecef 30%,#dfe6e6 70%,#c7a890 100%)" role="img" aria-label="Photograph of printed charts on a desk"><div class="abs date">21<br>FEB</div></div>
  <div class="abs post-title" style="left:666px">LOREM IPSUM DOLOR SIT AMET, CONSECTETUER ADIPISCING ELIT.</div>
  <p class="abs post-body" style="left:664px">Lorem ipsum dolor sit amet, consectetuer adipiscing elit. Aenean commodo ligula eget dolor. Aenean massa. Cum sociis natoque penatibus et magnis dis parturient montes, nascetur ridiculus mus. Donec quam felis,</p>
  <div class="abs link post-more" style="left:666px">READ MORE</div>

  <div class="abs photo" style="left:836px;background:linear-gradient(150deg,#4a6a2a 0%,#b89a6a 40%,#5a5a5a 70%,#c8a878 100%)" role="img" aria-label="Photograph of hands using a laptop on a table"><div class="abs date">25<br>JAN</div></div>
  <div class="abs post-title" style="left:838px">ELLUS. AENEAN LEO LIGULA, PORTTITOR EU, CONSEQUAT</div>
  <p class="abs post-body" style="left:838px">Nullam dictum felis eu pede mollis pretium. Integer tincidunt. Cras dapibus. Vivamus elementum semper nisi. Aenean vulputate eleifend tellus. Aenean leo ligula, porttitor eu, con-</p>
  <div class="abs link post-more" style="left:838px">READ MORE</div>

  <div class="abs photo" style="left:1011px;background:linear-gradient(150deg,#dcdcdc 0%,#a88a78 40%,#efefef 75%,#c8c8c8 100%)" role="img" aria-label="Photograph of a person working at a laptop"><div class="abs date">28<br>JUN</div></div>
  <div class="abs post-title" style="left:1015px">NULLAM DICTUM FELIS EU PEDE MOLLIS PRETIUM.</div>
  <p class="abs post-body" style="left:1014px">Phasellus viverra nulla ut metus varius laoreet. Quisque rutrum. Aenean imperdiet. Etiam ultricies nisi vel augue. Curabitur ullamcorper ultricies nisi. Nam eget dui. Etiam rhoncus. Maecenas tempus, tellus eget condi-</p>
  <div class="abs link post-more" style="left:1015px">READ MORE</div>
</section>

<section>
  <div class="abs contact"></div>
  <div class="abs map" role="img" aria-label="Street map of the harbour region and neighbouring islands"></div>
  <h3 class="abs contact-head">CONTACT<br>DETAILS</h3>
  <div class="abs contact-info">info@kestrelharbour.example<br>0900 555 0142</div>
</section>

<footer>
  <div class="abs footer"></div>
  <h3 class="abs foot-head" style="left:666px">HEAD<br>OFFICE</h3>
  <div class="abs foot-col" style="left:734px;width:110px"><b>MAIN OFFICE</b><br>&nbsp;&nbsp;Quisque rutrum. Aenean imperdiet. Etiam<br><br><b>Business Address:</b><br>Main Office<br>Lorem ipsum dolor sit amet, consectetuer adipiscing elit. Aenean commodo ligula eget dolor. Aenean massa. Cum sociis natoque</div>
  <div class="abs foot-col" style="left:852px"><b>Telephone:</b><br>(000) 555-0101<br>(000) 555-0102<br><br><b>Facsimile:</b><br>(000) 555-0103<br>(000) 555-0104</div>
  <h3 class="abs foot-head" style="left:941px">SERVICE<br>OFFICES</h3>
  <div class="abs foot-col" style="left:1014px;width:110px"><b>HARBOUR OFFICE</b><br>&nbsp;&nbsp;Quisque rutrum. Aenean imperdiet. Etiam<br><br><b>Business Address:</b><br>Lorem ipsum dolor sit amet, consectetuer adipiscing elit. Aenean commodo ligula eget dolor. Aenean massa. Cum sociis natoque penatibus et mag</div>
  <div class="abs foot-col" style="left:1132px"><b>Telephone:</b><br>(000) 555-0101<br>(000) 555-0102<br><br><b>Facsimile:</b><br>(000) 555-0103<br>(000) 555-0104</div>
  <div class="abs social" style="left:663px"></div>
  <div class="abs social" style="left:686px"></div>
  <div class="abs social" style="left:709px"></div>
  <div class="abs rights">©2018 All Rights Reserved</div>
</footer>
</body>
</html>
```